Website Redesign For Motorbike Rental Company In Thailand

We are a motorbike rental start up in Phuket, Thailand named RIDE ON.

We cater to the tourist and even ex pats that want to rent a motorbike for as short as only 3 days up to 1 year at a time.

We want a website that makes it a very simple ordering process for the customer. Be able to order a motorbike rental without scrolling down...

Simple, attractive design that builds trust and credibility is huge.

Please check this google doc for the CONTENT: https://files.velmora-docs.example/sheet/7KqT2wXbRn4LpZ9cYmHfJd3sVa8GtEu1NoBiQrWk/view?mode=share

Target Market(s)

Tourists In Thailand & Expats In Thailand

Industry/Entity Type

motorbike rental, motorcycle rental

Number of Pages Required

1 page

Requirements
Must have
• Must have a thailand phuket theme or feel
Nice to have
• We want a website that makes it a very simple ordering process for the customer. Be able to order a motorbike rental without scrolling down... Simple, attractive design that builds trust and credibility is huge.
Should not have
• na

```html
<!DOCTYPE html>
<html lang="en">
<head>
<meta charset="utf-8">
<title>RIDE ON – Motorbike Rentals in Phuket</title>
<link href="https://fonts.googleapis.com/css2?family=Josefin+Sans:wght@400;600;700&display=swap" rel="stylesheet">
<style>
:root{
  --orange:#f07a14;
  --orange-deep:#e86f0b;
  --ink:#1d1d1d;
  --text:#333;
  --muted:#777;
  --page:#f7f7f7;
  --line:#dcdcdc;
  --card-grey:#efefef;
  --card-peach:#fdeee3;
  --card-mint:#dcf7e8;
  --dark:#1e2230;
  --frame:#6b6b6b;
  --field:#f0f0f0;
}
*{box-sizing:border-box;margin:0;padding:0}
html,body{width:929px;height:1200px;overflow:hidden;background:#fff}
body{font-family:'Josefin Sans',sans-serif;color:var(--text);position:relative}
.abs{position:absolute}
.desktop{position:absolute;left:0;top:0;width:562px;height:1200px;background:var(--page);overflow:hidden}
.gutter{position:absolute;left:562px;top:0;width:60px;height:1200px;background:var(--frame)}
.hero-photo{left:0;top:0;width:562px;height:310px;background:linear-gradient(135deg,#3b4150,#1e2028 55%,#4a3a36)}
.navbar{left:36px;top:14px;width:484px;height:49px;background:#fff;display:flex;align-items:center}
.brand{position:absolute;left:10px;top:15px;display:flex;align-items:center;gap:4px;font-weight:700;font-size:13px;color:var(--orange)}
.brand-dot{width:10px;height:10px;border-radius:50%;background:var(--orange)}
.nav-link{position:absolute;top:22px;font-size:9.5px;color:var(--ink)}
.nav-phone{position:absolute;left:378px;top:17px;display:flex;align-items:center;gap:5px;font-size:9px;color:var(--ink)}
.phone-badge{width:18px;height:18px;border-radius:50%;background:var(--orange);display:flex;align-items:center;justify-content:center}
.hero-title{left:35px;top:120px;font-size:30px;line-height:33px;font-weight:700;color:#fff}
.btn-orange{background:var(--orange);color:#fff;font-weight:700;display:flex;align-items:center;justify-content:center}
.hero-btn{left:36px;top:236px;width:114px;height:33px;font-size:12px}
.form-card{left:293px;top:96px;width:227px;height:254px;background:#fff;box-shadow:0 2px 8px rgba(0,0,0,.08)}
.form-title{position:absolute;top:18px;width:100%;text-align:center;font-size:16px;font-weight:700;color:var(--ink)}
.form-title span{color:var(--orange)}
.field{position:absolute;left:15px;width:196px;height:25px;background:var(--field);border:1px solid #e2e2e2;font-size:7px;color:#999;display:flex;align-items:center;padding:0 5px;justify-content:space-between}
.field.dark{color:#333}
.form-submit{position:absolute;left:15px;top:187px;width:196px;height:25px;font-size:9.5px}
.form-note{position:absolute;top:222px;width:100%;text-align:center;font-size:8.5px;color:#555}
.ornament{display:flex;align-items:center;justify-content:center;gap:4px}
.ornament i{display:block;width:28px;height:1px;background:#555}
.ornament b{display:block;width:22px;height:22px;border-radius:50%;background:var(--orange)}
.section-title{font-size:27px;font-weight:700;color:#333;text-align:center}
.step-art{left:0;top:441px;width:149px;height:104px;background:linear-gradient(90deg,#e8741c,#6b4a2c)}
.step{top:438px;width:114px;height:114px;padding:8px 6px;font-size:10.5px;line-height:13px;color:#444;overflow:hidden}
.step em{position:absolute;right:-2px;bottom:-8px;font-style:normal;font-size:56px;font-weight:700;color:#fff}
.btn-black{left:231px;top:579px;width:106px;height:21px;background:#000;color:#fff;font-size:9.5px;font-weight:700;display:flex;align-items:center;justify-content:center}
.rule{left:0;top:622px;width:562px;height:1px;background:var(--line)}
.photo{background:linear-gradient(135deg,#8a8f7a,#55624a)}
.features-list{left:261px;top:798px;list-style:none;font-size:7px;line-height:11px;color:#444}
.features-list li{display:flex;align-items:center;gap:4px}
.features-list li::before{content:"";width:5px;height:5px;border:1px solid var(--orange)}
.orange-band{left:0;top:907px;width:562px;height:236px;background:var(--orange)}
.bike-card{top:994px;width:154px;height:220px;background:#fff}
.bike-pic{position:absolute;left:10px;top:6px;width:134px;height:92px;background:linear-gradient(135deg,#e5e5e5,#a9a9a9)}
.bike-price{position:absolute;top:104px;width:100%;text-align:center;font-size:12px;font-weight:600;color:var(--ink)}
.bike-name{position:absolute;left:28px;top:121px;width:97px;height:17px;font-size:10px;font-weight:400}
.spec{position:absolute;left:0;width:100%;height:21px;border-bottom:1px solid #e8e8e8;font-size:6.5px;color:#333;display:flex;align-items:center;padding-left:3px}
.spec .k{width:68px;padding-left:10px;position:relative}
.spec .k::before{content:"✓";position:absolute;left:0;color:var(--orange);font-weight:700}
/* thumbnail */
.thumb{position:absolute;left:664px;top:0;width:210px;height:1193px;background:var(--page);overflow:hidden}
.t{position:absolute}
.tiny{font-size:3.4px;line-height:4.4px;color:#555}
.tcenter{text-align:center;width:100%;left:0}
</style>
</head>
<body>

<section class="desktop">
  <div class="abs hero-photo" role="img" aria-label="Photo of parked scooters on a Phuket street"></div>
  <header class="abs navbar">
    <div class="brand"><span class="brand-dot"></span>RIDE ON</div>
    <span class="nav-link" style="left:137px">Rservation</span>
    <span class="nav-link" style="left:198px">Prices</span>
    <span class="nav-link" style="left:243px">Terms</span>
    <span class="nav-link" style="left:286px">FAQ</span>
    <span class="nav-link" style="left:324px">Contact</span>
    <div class="nav-phone"><span class="phone-badge"><svg width="9" height="9" viewBox="0 0 24 24"><path fill="#fff" d="M6.6 10.8a15 15 0 006.6 6.6l2.2-2.2a1 1 0 011-.25 11.4 11.4 0 003.6.57 1 1 0 011 1V20a1 1 0 01-1 1A17 17 0 013 4a1 1 0 011-1h3.5a1 1 0 011 1 11.4 11.4 0 00.57 3.6 1 1 0 01-.25 1z"/></svg></span>+66 7600 555 210</div>
  </header>
  <h1 class="abs hero-title">Fast Motorbike<br>Rentals In<br>Phuket, Thailand</h1>
  <a class="abs btn-orange hero-btn">VIEW OUR BIKES</a>

  <form class="abs form-card">
    <div class="form-title"><span>Reserve</span> a city bikes</div>
    <div class="field" style="top:49px">Pick -Up <svg width="13" height="12" viewBox="0 0 13 12"><rect x=".5" y="1.5" width="12" height="10" fill="none" stroke="#333"/><path d="M0 4h13M3 0v3M10 0v3M3 6h7M3 8h7M3 10h7" stroke="#333" stroke-width=".7"/></svg></div>
    <div class="field" style="top:83px">Drop - Off <svg width="13" height="12" viewBox="0 0 13 12"><rect x=".5" y="1.5" width="12" height="10" fill="none" stroke="#333"/><path d="M0 4h13M3 0v3M10 0v3M3 6h7M3 8h7M3 10h7" stroke="#333" stroke-width=".7"/></svg></div>
    <div class="field" style="top:117px;justify-content:flex-start;gap:3px"><svg width="11" height="7"><rect width="11" height="7" fill="#a51931"/><rect y="1.2" width="11" height="4.6" fill="#fff"/><rect y="2.3" width="11" height="2.4" fill="#2d2a4a"/></svg>▾ <b style="color:#333;font-weight:400">+66</b> 7600 555 210</div>
    <div class="field dark" style="top:151px">Choose Motorbike <span>▾</span></div>
    <button class="btn-orange form-submit" type="button" style="border:0;font-family:inherit">Quick Request →</button>
    <p class="form-note">*Best deal guaranteed in minutes!</p>
  </form>

  <div class="abs ornament" style="left:200px;top:363px"><i></i><b></b><i></i></div>
  <h2 class="abs section-title" style="left:0;top:392px;width:552px">How It Works</h2>
  <div class="abs step-art" role="img" aria-label="Illustration of an orange motorbike"></div>
  <div class="abs step" style="left:161px;background:var(--card-grey)">Choose<br>Your Bike<em>1</em></div>
  <div class="abs step" style="left:283px;background:var(--card-peach)">Enter Rental Date Period &amp; Enter Delivery Address Or Choose To Pick Up<em>2</em></div>
  <div class="abs step" style="left:405px;background:var(--card-mint)">Get Your Bike Delivered In Less Than 2 Hours Or Pick Up ASAP!<em>3</em></div>
  <a class="abs btn-black">Start Your Search →</a>
  <div class="abs rule"></div>

  <h2 class="abs" style="left:35px;top:653px;font-size:20px;line-height:22px;font-weight:700;color:#333">Fast Motorbike Rentals<br>In Phuket, Thailand</h2>
  <div class="abs photo" style="left:0;top:712px;width:245px;height:158px" role="img" aria-label="Photo of a couple on a scooter reading a map"></div>
  <div class="abs photo" style="left:261px;top:654px;width:208px;height:114px;background:linear-gradient(135deg,#8e9aa6,#5e6a64)" role="img" aria-label="Photo of a rider on a busy Phuket street"></div>
  <div class="abs photo" style="left:481px;top:654px;width:81px;height:114px;background:linear-gradient(135deg,#7a8a6e,#4a5548)" role="img" aria-label="Photo of a narrow town street"></div>
  <h3 class="abs" style="left:261px;top:775px;font-size:17px;font-weight:700;color:#333">Renting Service Features</h3>
  <ul class="abs features-list">
    <li>Free Delivery &amp; Pick Up Anywhere In Phuket</li>
    <li>Free High Quality Helmet Included</li>
    <li>Free Unlimited Mileage</li>
    <li>Easy &amp; Quick Online Booking</li>
    <li>No Credit Card Required</li>
    <li>Pay When Bike Is Delivered</li>
    <li>Speak English &amp; Thai</li>
  </ul>

  <div class="abs orange-band"></div>
  <h2 class="abs section-title" style="left:0;top:938px;width:552px;color:#fff">Choose Your Bike</h2>
  <article class="abs bike-card" style="left:36px">
    <div class="bike-pic" role="img" aria-label="Photo of a grey automatic scooter"></div>
    <div class="bike-price">200 Baht/Day</div>
    <div class="btn-orange bike-name">Breeze 150</div>
    <div class="spec" style="top:156px"><span class="k">Transmission</span>Automatic</div>
    <div class="spec" style="top:177px"><span class="k">Engine Capacity</span>150 cc</div>
  </article>
  <article class="abs bike-card" style="left:201px">
    <div class="bike-pic" role="img" aria-label="Photo of a blue automatic scooter"></div>
    <div class="bike-price">225 Baht/Day</div>
    <div class="btn-orange bike-name">Cruiser 160</div>
    <div class="spec" style="top:156px"><span class="k">Transmission</span>Automatic</div>
    <div class="spec" style="top:177px"><span class="k">Engine Capacity</span>153cc</div>
  </article>
  <article class="abs bike-card" style="left:366px">
    <div class="bike-pic" role="img" aria-label="Photo of a black touring scooter"></div>
    <div class="bike-price">400 Baht/Day</div>
    <div class="btn-orange bike-name">Tourer 300</div>
    <div class="spec" style="top:156px"><span class="k">Transmission</span>Automatic</div>
    <div class="spec" style="top:177px"><span class="k">Engine Capacity</span>279 cc</div>
  </article>
</section>

<div class="gutter"></div>

<section class="thumb">
  <div class="t" style="left:0;top:0;width:210px;height:114px;background:linear-gradient(135deg,#3b4150,#1e2028 55%,#4a3a36)" role="img" aria-label="Photo of parked scooters"></div>
  <div class="t" style="left:16px;top:5px;width:179px;height:18px;background:#fff"></div>
  <div class="t" style="left:19px;top:11px;font-size:5px;font-weight:700;color:var(--orange)">RIDE ON</div>
  <div class="t tiny" style="left:67px;top:12px;color:#222;word-spacing:4px">Rservation Prices Terms FAQ Contact</div>
  <div class="t" style="left:156px;top:10px;width:6px;height:6px;border-radius:50%;background:var(--orange)"></div>
  <div class="t tiny" style="left:164px;top:12px;color:#222">+66 7600 555 210</div>
  <div class="t" style="left:16px;top:44px;font-size:10px;line-height:12px;font-weight:700;color:#fff">Fast Motorbike<br>Rentals In<br>Phuket, Thailand</div>
  <div class="t btn-orange" style="left:16px;top:87px;width:42px;height:11px;font-size:4px">VIEW OUR BIKES</div>
  <div class="t" style="left:111px;top:35px;width:84px;height:94px;background:#fff"></div>
  <div class="t" style="left:111px;top:41px;width:84px;text-align:center;font-size:5px;font-weight:700">
    <span style="color:var(--orange)">Reserve</span> a city bikes</div>
  <div class="t tiny" style="left:117px;top:54px;width:72px;height:8px;background:var(--field);padding:2px">Pick -Up</div>
  <div class="t tiny" style="left:117px;top:66px;width:72px;height:8px;background:var(--field);padding:2px">Drop - Off</div>
  <div class="t tiny" style="left:117px;top:78px;width:72px;height:8px;background:var(--field);padding:2px">+66 7600 555 210</div>
  <div class="t tiny" style="left:117px;top:90px;width:72px;height:8px;background:var(--field);padding:2px">Choose Motorbike</div>
  <div class="t btn-orange" style="left:117px;top:104px;width:72px;height:8px;font-size:3.5px">Quick Request →</div>
  <div class="t tiny tcenter" style="left:111px;width:84px;top:117px">*Best deal guaranteed in minutes!</div>

  <div class="t" style="left:101px;top:134px;width:8px;height:8px;border-radius:50%;background:var(--orange)"></div>
  <div class="t tcenter" style="top:145px;font-size:9px;font-weight:700">How It Works</div>
  <div class="t" style="left:0;top:162px;width:58px;height:40px;background:linear-gradient(90deg,#e8741c,#6b4a2c)" role="img" aria-label="Illustration of an orange motorbike"></div>
  <div class="t tiny" style="left:63px;top:162px;width:42px;height:41px;background:var(--card-grey);padding:3px">Choose Your Bike</div>
  <div class="t tiny" style="left:107px;top:162px;width:43px;height:41px;background:var(--card-peach);padding:3px">Enter Rental Date Period &amp; Enter Delivery Address Or Choose To Pick Up</div>
  <div class="t tiny" style="left:152px;top:162px;width:43px;height:41px;background:var(--card-mint);padding:3px">Get Your Bike Delivered In Less Than 2 Hours Or Pick Up ASAP!</div>
  <div class="t" style="left:89px;top:214px;width:38px;height:7px;background:#000;color:#fff;font-size:3px;display:flex;align-items:center;justify-content:center">Start Your Search →</div>
  <div class="t" style="left:0;top:230px;width:210px;height:1px;background:var(--line)"></div>

  <div class="t" style="left:16px;top:241px;font-size:6.5px;line-height:8px;font-weight:700">Fast Motorbike Rentals<br>In Phuket, Thailand</div>
  <div class="t photo" style="left:0;top:262px;width:94px;height:59px" role="img" aria-label="Photo of a couple on a scooter"></div>
  <div class="t photo" style="left:100px;top:241px;width:77px;height:42px;background:linear-gradient(135deg,#8e9aa6,#5e6a64)" role="img" aria-label="Photo of a street scene"></div>
  <div class="t photo" style="left:181px;top:241px;width:29px;height:42px;background:linear-gradient(135deg,#7a8a6e,#4a5548)" role="img" aria-label="Photo of a town street"></div>
  <div class="t" style="left:100px;top:286px;font-size:6px;font-weight:700">Renting Service Features</div>
  <div class="t" style="left:100px;top:294px;font-size:2.6px;line-height:4px;color:#555">Free Delivery &amp; Pick Up Anywhere In Phuket<br>Free High Quality Helmet Included<br>Free Unlimited Mileage<br>Easy &amp; Quick Online Booking<br>No Credit Card Required<br>Pay When Bike Is Delivered<br>Speak English &amp; Thai</div>

  <div class="t" style="left:0;top:334px;width:210px;height:88px;background:var(--orange)"></div>
  <div class="t tcenter" style="top:347px;font-size:8px;font-weight:700;color:#fff">Choose Your Bike</div>
  <div class="t" style="left:16px;top:367px;width:57px;height:144px;background:#fff"></div>
  <div class="t" style="left:78px;top:367px;width:56px;height:144px;background:#fff"></div>
  <div class="t" style="left:138px;top:367px;width:57px;height:144px;background:#fff"></div>
  <div class="t" style="left:21px;top:369px;width:47px;height:34px;background:linear-gradient(135deg,#e5e5e5,#a9a9a9)" role="img" aria-label="Photo of a grey scooter"></div>
  <div class="t" style="left:83px;top:369px;width:46px;height:34px;background:linear-gradient(135deg,#e5e5e5,#7c93b4)" role="img" aria-label="Photo of a blue scooter"></div>
  <div class="t" style="left:143px;top:369px;width:47px;height:34px;background:linear-gradient(135deg,#e5e5e5,#888)" role="img" aria-label="Photo of a black scooter"></div>
  <div class="t tiny" style="left:16px;top:405px;width:57px;text-align:center;color:#222">200 Baht/Day</div>
  <div class="t tiny" style="left:78px;top:405px;width:56px;text-align:center;color:#222">225 Baht/Day</div>
  <div class="t tiny" style="left:138px;top:405px;width:57px;text-align:center;color:#222">400 Baht/Day</div>
  <div class="t btn-orange" style="left:27px;top:411px;width:35px;height:5px;font-size:3px">Breeze 150</div>
  <div class="t btn-orange" style="left:89px;top:411px;width:34px;height:5px;font-size:3px">Cruiser 160</div>
  <div class="t btn-orange" style="left:149px;top:411px;width:35px;height:5px;font-size:3px">Tourer 300</div>
  <div class="t" style="left:18px;top:426px;font-size:2.4px;line-height:7.7px;color:#444">Transmission · Automatic<br>Engine Capacity · 150 cc<br>Curb weight · 106 kg<br>Fuel Tank Volume · 5.5 L<br>Range · About 200 km<br>Top Speed · 110 km/h<br>Power Output · 9 kW<br>Maximum Torque · 14 Nm<br>Fuel Use · 50 km per L</div>
  <div class="t" style="left:80px;top:426px;font-size:2.4px;line-height:7.7px;color:#444">Transmission · Automatic<br>Engine Capacity · 153cc<br>Curb weight · 130 kg<br>Fuel Tank Volume · 8 L<br>Range · About 300 km<br>Top Speed · 115 km/h<br>Power Output · 10 kW<br>Maximum Torque · 14 Nm<br>Fuel Use · 45 km per L</div>
  <div class="t" style="left:140px;top:426px;font-size:2.4px;line-height:7.7px;color:#444">Transmission · Automatic<br>Engine Capacity · 279 cc<br>Curb weight · 182 kg<br>Fuel Tank Volume · 11.5 L<br>Range · About 350 km<br>Top Speed · 135 km/h<br>Power Output · 18 kW<br>Maximum Torque · 27 Nm<br>Fuel Use · 30 km per L</div>
  <div class="t" style="left:16px;top:501px;width:57px;text-align:center;font-size:3px;color:var(--orange);font-weight:700">RENT BIKE NOW</div>
  <div class="t" style="left:78px;top:501px;width:56px;text-align:center;font-size:3px;color:var(--orange);font-weight:700">RENT BIKE NOW</div>
  <div class="t" style="left:138px;top:501px;width:57px;text-align:center;font-size:3px;color:var(--orange);font-weight:700">RENT BIKE NOW</div>
  <div class="t" style="left:101px;top:521px;width:6px;height:6px;background:#111"></div>
  <div class="t" style="left:109px;top:521px;width:6px;height:6px;background:#111"></div>

  <div class="t" style="left:0;top:537px;width:210px;height:129px;background:var(--dark)"></div>
  <div class="t" style="left:101px;top:545px;width:8px;height:8px;border-radius:50%;background:var(--orange)"></div>
  <div class="t tcenter" style="top:558px;font-size:8.5px;font-weight:700;color:#fff">Why Choose RIDE ON</div>
  <div class="t" style="left:72px;top:579px;width:66px;height:66px;border-radius:50%;background:var(--orange);border:2px solid #fff" role="img" aria-label="Illustration of a rider on a sport motorbike"></div>
  <div class="t" style="left:16px;top:581px;width:53px;text-align:right;font-size:4.5px;line-height:5px;color:#fff">Fully Insure<br>Rental Service</div>
  <div class="t" style="left:16px;top:593px;width:53px;text-align:right;font-size:2.3px;line-height:3px;color:#bbb">Every rental comes fully insured for a calm and safe ride.</div>
  <div class="t" style="left:16px;top:617px;width:53px;text-align:right;font-size:4.5px;line-height:5px;color:#fff">Different Types<br>Of Bikes</div>
  <div class="t" style="left:16px;top:629px;width:53px;text-align:right;font-size:2.3px;line-height:3px;color:#bbb">Pick from scooters, cruisers and tourers for any trip.</div>
  <div class="t" style="left:146px;top:581px;width:53px;font-size:4.5px;line-height:5px;color:#fff">Fully Insure<br>Rental Service</div>
  <div class="t" style="left:146px;top:593px;width:53px;font-size:2.3px;line-height:3px;color:#bbb">Every rental comes fully insured for a calm and safe ride.</div>
  <div class="t" style="left:146px;top:617px;width:53px;font-size:4.5px;line-height:5px;color:#fff">Different Types<br>Of Bikes</div>
  <div class="t" style="left:146px;top:629px;width:53px;font-size:2.3px;line-height:3px;color:#bbb">Pick from scooters, cruisers and tourers for any trip.</div>

  <div class="t" style="left:101px;top:672px;width:7px;height:7px;border-radius:50%;background:var(--orange)"></div>
  <div class="t tcenter" style="top:685px;font-size:8px;font-weight:700">Free Helmets</div>
  <div class="t" style="left:16px;top:702px;width:41px;height:40px;background:linear-gradient(135deg,#eee,#b9a77a)" role="img" aria-label="Photo of an open-face helmet"></div>
  <div class="t" style="left:63px;top:702px;width:40px;height:40px;background:linear-gradient(135deg,#eee,#b9a77a)" role="img" aria-label="Photo of an open-face helmet"></div>
  <div class="t" style="left:110px;top:702px;width:40px;height:40px;background:linear-gradient(135deg,#eee,#b9a77a)" role="img" aria-label="Photo of an open-face helmet"></div>
  <div class="t" style="left:156px;top:702px;width:40px;height:40px;background:linear-gradient(135deg,#eee,#b9a77a)" role="img" aria-label="Photo of an open-face helmet"></div>

  <div class="t" style="left:0;top:752px;width:210px;height:110px;background:var(--orange)"></div>
  <div class="t" style="left:101px;top:762px;width:7px;height:7px;border-radius:50%;background:#fff"></div>
  <div class="t tcenter" style="top:774px;font-size:8px;font-weight:700;color:#fff">FAQ</div>
  <div class="t" style="left:34px;top:790px;width:147px;height:57px;background:#fff"></div>
  <div class="t tiny" style="left:37px;top:795px;width:141px;font-size:2.8px;line-height:14.3px;color:#333">How do I book a bike for my stay? <span style="float:right">+</span><br>Can the bike be delivered to my hotel? <span style="float:right">+</span><br>What do I need to show on delivery? <span style="float:right">+</span><br>How long can I rent a motorbike? <span style="float:right">+</span></div>

  <div class="t" style="left:0;top:862px;width:210px;height:123px;background:linear-gradient(135deg,#3b4150,#1f242c)" role="img" aria-label="Photo of a rider on a city street"></div>
  <div class="t" style="left:63px;top:874px;width:84px;height:111px;background:#fff"></div>
  <div class="t" style="left:63px;top:880px;width:84px;text-align:center;font-size:5px;font-weight:700"><span style="color:var(--orange)">Reserve</span> a city bikes</div>
  <div class="t tiny" style="left:69px;top:893px;width:72px;height:7px;background:var(--field);padding:1.5px">Pick -Up</div>
  <div class="t tiny" style="left:69px;top:905px;width:72px;height:7px;background:var(--field);padding:1.5px">Drop - Off</div>
  <div class="t tiny" style="left:69px;top:917px;width:72px;height:7px;background:var(--field);padding:1.5px">+66 7600 555 210</div>
  <div class="t tiny" style="left:69px;top:929px;width:72px;height:7px;background:var(--field);padding:1.5px">Choose Motorbike</div>
  <div class="t tiny" style="left:69px;top:942px;width:72px;height:7px;background:var(--field);padding:1.5px">Point</div>
  <div class="t btn-orange" style="left:69px;top:955px;width:72px;height:8px;font-size:3.5px">BOOKING →</div>

  <div class="t" style="left:0;top:985px;width:210px;height:104px;background:linear-gradient(135deg,#dfe8d8,#c9d9e4)" role="img" aria-label="Map of Phuket town"></div>
  <div class="t" style="left:16px;top:996px;width:59px;height:44px;background:#fff;padding:5px"><div style="font-size:6px;font-weight:700">Contact Us</div><div style="font-size:2.8px;line-height:4px;color:#555;margin-top:3px">+66 7600 555 210<br>hello@rideon.example<br>Address line goes here.</div></div>

  <div class="t" style="left:0;top:1107px;width:210px;height:86px;background:#222"></div>
  <div class="t btn-orange" style="left:16px;top:1094px;width:179px;height:31px;font-size:8.5px;line-height:10px;text-align:center">Fast Motorbike Rentals In<br>Phuket, Thailand</div>
  <div class="t tcenter" style="top:1136px;font-size:6px;color:#fff">+66 7600 555 210</div>
  <div class="t tcenter" style="top:1151px;font-size:2.8px;color:#ddd;word-spacing:4px">Rservation Prices Terms FAQ Contact</div>
  <div class="t" style="left:78px;top:1167px;width:11px;height:10px;background:var(--orange)"></div>
  <div class="t" style="left:93px;top:1167px;width:11px;height:10px;background:var(--orange)"></div>
  <div class="t" style="left:108px;top:1167px;width:11px;height:10px;background:var(--orange)"></div>
  <div class="t" style="left:123px;top:1167px;width:11px;height:10px;background:var(--orange)"></div>
  <div class="t tcenter" style="top:1184px;font-size:2.4px;color:#aaa">Copyright RIDE ON 2024. All rights reserved.</div>
</section>

</body>
</html>
```